Luxury Home Builder looking for an Exciting Homes Portfolio

We have a number of custom homes that we have completed over the years, and we want to give prospective clients are colorful and exciting catalog of our previous homes. I will provide access to the dropbox with all the photos. Need to get as many photos of homes in the catalog as possible. Please use talvinecrestbuilds.com for pictures, lots of them in the portfolio, projects in progress, spec homes are available. I will provide full files to the winner. Need a very hip catalog to give out at events, and marketing venues.

Target Market(s)

High Net Worth Individuals looking for luxury homes

Industry/Entity Type

Real Estate Development

Requirements
Must have
• Photos of our project, please use talvinecrestbuilds.com to get the photos, and will provide access to full pictures on dropbox to the winner.
• Logo must be incorporated.
Nice to have
• Clarification, website is not for design, but for the purposes of getting the photos. this has to be a very cool portfolio.

```html
<!DOCTYPE html>
<html lang="en">
<head>
<meta charset="UTF-8">
<title>Talvine Crest – Portfolio Spread</title>
<link href="https://fonts.googleapis.com/css2?family=Open+Sans:ital,wght@0,400;0,600;0,700;0,800;1,400&display=swap" rel="stylesheet">
<style>
  :root{
    --stage:#ededed;
    --paper:#ffffff;
    --ink:#4a4a4a;
    --ink-soft:#8a8a8a;
    --brand-red:#e2262b;
    --brand-orange:#f07d1a;
    --brand-blue:#2b5ea8;
    --brand-blue-deep:#1d3f7a;
    --rule:#d9d9d9;
  }
  *{box-sizing:border-box;margin:0;padding:0}
  html,body{width:1200px;height:900px;overflow:hidden}
  body{background:var(--stage);font-family:"Open Sans",Arial,sans-serif;color:var(--ink);position:relative}

  .spread{position:absolute;left:50px;top:255px;width:1100px;height:390px;display:flex;box-shadow:0 18px 40px rgba(0,0,0,.18)}
  .page{position:relative;width:550px;height:390px;overflow:hidden;background:var(--paper)}
  .page--left::after{content:"";position:absolute;top:0;right:0;width:40px;height:100%;background:linear-gradient(90deg,rgba(0,0,0,0),rgba(0,0,0,.18))}
  .page--right::before{content:"";position:absolute;top:0;left:0;width:40px;height:100%;background:linear-gradient(90deg,rgba(0,0,0,.12),rgba(0,0,0,0));z-index:1}

  .hero-photo{position:absolute;inset:0;background:linear-gradient(180deg,#1c2a6e 0%,#3a4f8f 38%,#5d6478 58%,#8b7552 76%,#5a4a3a 100%)}

  .contents{position:absolute;left:38px;top:30px;width:205px;height:305px;background:rgba(255,255,255,.86);padding:18px 16px 12px}
  .contents__title{font-size:22px;font-weight:800;color:var(--brand-red);letter-spacing:-.3px;margin-bottom:14px}
  .contents__item{border-bottom:1px solid var(--rule);padding:6px 0 6px}
  .contents__heading{font-size:8.5px;font-weight:700;color:var(--brand-blue-deep);text-transform:uppercase;letter-spacing:.3px}
  .contents__sub{display:flex;justify-content:space-between;font-size:7px;color:var(--ink-soft);margin-top:2px}
  .contents__brand{position:absolute;left:16px;bottom:14px;display:flex;align-items:center;gap:6px}

  .brand-mark{display:flex;align-items:center;gap:7px}
  .brand-mark__dot{width:16px;height:16px;border-radius:50%;background:var(--brand-blue)}
  .brand-mark__name{font-size:10px;font-weight:700;letter-spacing:2px;color:var(--brand-blue-deep)}

  .page-wave{position:absolute;left:0;bottom:0;width:100%;height:48px}

  .ribbon{position:absolute;left:0;top:42px;width:300px;height:26px}
  .ribbon__label{position:absolute;left:38px;top:5px;font-size:12px;font-weight:700;color:#fff;letter-spacing:.5px}

  .about__text{position:absolute;left:80px;top:98px;width:400px;font-size:8.5px;line-height:1.75;font-style:italic;color:var(--ink)}

  .features{position:absolute;left:55px;top:200px;display:flex;gap:28px}
  .feature{width:74px;height:74px;border-radius:50%;background:radial-gradient(circle at 40% 35%,#ffffff,#ececec);box-shadow:0 4px 10px rgba(0,0,0,.22);display:flex;flex-direction:column;align-items:center;justify-content:center;gap:3px}
  .feature svg{width:20px;height:20px}
  .feature__label{font-size:6.5px;font-weight:600;text-align:center;color:var(--ink);text-transform:uppercase;line-height:1.2}

  .about__brand{position:absolute;right:32px;bottom:62px}
</style>
</head>
<body>
  <main class="spread">
    <section class="page page--left">
      <div class="hero-photo" role="img" aria-label="Dusk photograph of a luxury home with a lit swimming pool and terrace"></div>

      <nav class="contents">
        <h2 class="contents__title">Contents</h2>
        <div class="contents__item">
          <div class="contents__heading">Our Brand</div>
          <div class="contents__sub"><span>Heritage, vision and values</span><span>02</span></div>
        </div>
        <div class="contents__item">
          <div class="contents__heading">Our Products</div>
          <div class="contents__sub"><span>Homes, finishes and options</span><span>06</span></div>
        </div>
        <div class="contents__item">
          <div class="contents__heading">Our Support Structure</div>
          <div class="contents__sub"><span>Teams that guide every build</span><span>12</span></div>
        </div>
        <div class="contents__item">
          <div class="contents__heading">Building Your Dessert Bar</div>
          <div class="contents__sub"><span>Planning your perfect space</span><span>16</span></div>
        </div>
        <div class="contents__item">
          <div class="contents__heading">Marketing and Promotions</div>
          <div class="contents__sub"><span>Events, media and outreach</span><span>20</span></div>
        </div>
        <div class="contents__brand brand-mark">
          <span class="brand-mark__dot"></span>
          <span class="brand-mark__name">TALVINE CREST</span>
        </div>
      </nav>

      <svg class="page-wave" viewBox="0 0 550 48" preserveAspectRatio="none" aria-hidden="true">
        <path d="M0 22 Q300 30 550 8 L550 48 L0 48Z" fill="var(--brand-blue)"/>
        <path d="M0 22 Q300 30 550 8" fill="none" stroke="var(--brand-orange)" stroke-width="2"/>
      </svg>
    </section>

    <section class="page page--right">
      <svg class="ribbon" viewBox="0 0 300 26" preserveAspectRatio="none" aria-hidden="true">
        <defs>
          <linearGradient id="ribbonFill" x1="0" x2="1" y1="0" y2="0">
            <stop offset="0" stop-color="#f49a1e"/>
            <stop offset=".45" stop-color="#e2262b"/>
            <stop offset=".7" stop-color="#b9b9b9"/>
            <stop offset="1" stop-color="#ffffff" stop-opacity="0"/>
          </linearGradient>
        </defs>
        <path d="M0 0 H300 L300 26 H0Z" fill="url(#ribbonFill)"/>
      </svg>
      <span class="ribbon__label" style="position:absolute;left:38px;top:47px">ABOUT US</span>

      <p class="about__text">Talvine Crest has shaped distinctive residences for over two decades, pairing refined architecture with careful craftsmanship. Every home begins with a conversation about how you live, then grows through thoughtful planning, premium materials and a dedicated team. From spec homes to fully custom estates, we deliver spaces built for comfort, beauty and lasting value for every family we serve.</p>

      <div class="features">
        <div class="feature">
          <svg viewBox="0 0 20 20" aria-hidden="true"><path d="M3 10 L10 3 L17 10 M5 9 V17 H15 V9" fill="none" stroke="#333" stroke-width="1.8"/></svg>
          <span class="feature__label">Custom<br>Homes</span>
        </div>
        <div class="feature">
          <svg viewBox="0 0 20 20" aria-hidden="true"><circle cx="7" cy="7" r="3" fill="#333"/><circle cx="13" cy="7" r="3" fill="#333"/><path d="M2 17 Q7 10 12 17Z M8 17 Q13 10 18 17Z" fill="#333"/></svg>
          <span class="feature__label">Design<br>Team</span>
        </div>
        <div class="feature">
          <svg viewBox="0 0 20 20" aria-hidden="true"><rect x="3" y="6" width="14" height="10" rx="2" fill="#333"/><rect x="7" y="4" width="6" height="3" fill="#333"/><circle cx="10" cy="11" r="3" fill="#fff"/></svg>
          <span class="feature__label">Spec<br>Homes</span>
        </div>
        <div class="feature">
          <svg viewBox="0 0 20 20" aria-hidden="true"><path d="M3 16 L9 10 M11 8 L16 3 M13 3 H16 V6" fill="none" stroke="#333" stroke-width="1.8"/><path d="M3 4 L7 8 L5 10 L1 6Z" fill="#333"/></svg>
          <span class="feature__label">Build<br>Process</span>
        </div>
      </div>

      <div class="about__brand brand-mark">
        <span class="brand-mark__dot"></span>
        <span class="brand-mark__name">TALVINE CREST</span>
      </div>

      <svg class="page-wave" viewBox="0 0 550 48" preserveAspectRatio="none" aria-hidden="true">
        <path d="M0 10 Q260 20 550 38 L550 48 L0 48Z" fill="var(--brand-blue)"/>
        <path d="M0 10 Q260 20 550 38" fill="none" stroke="var(--brand-orange)" stroke-width="2"/>
      </svg>
    </section>
  </main>
</body>
</html>
```